HARD MONEY ORIGINATOR RECRUITMENT.
Looking for individuals to help us originate loans for real estate investor financing primarily used to fix up properties and resell.
HARD MONEY ORIGINATORS WANTED
No Licensing Required
Work As Independent Contractor
1% Flat Finders Fee on Each Loan
Referral Compensation for Recruiting New Originators
Immediate Payouts
Programs Offered Nationwide
Marketing Assistance and Support Available
Email mpelton@brightquaylending.com for more information or call (800) 641-2950 Ext. 24 Brightquay Lending Services, Inc. www.brightquaylending.com NMLS #318760
Industry/Entity Type
Real Estate
Look and feel
Each slider illustrates characteristics of the customer's brand and the style your logo design should communicate.

```html
<!DOCTYPE html>
<html lang="en">
<head>
<meta charset="utf-8">
<title>Hard Money Originators Wanted – Brightquay Lending Services, Inc.</title>
<link rel="stylesheet" href="https://fonts.googleapis.com/css2?family=Montserrat:wght@300;400;500;600;700&display=swap">
<style>
  :root {
    --canvas-bg: #eef0f3;
    --paper: #ffffff;
    --brand-blue: #1565b4;
    --brand-blue-light: #3f8fd4;
    --brand-blue-deep: #0f4f95;
    --cream: #e9e4c6;
    --ink: #1b1b1b;
    --photo-warm: #c9a860;
    --photo-green: #7f9a55;
    --photo-sky: #c7d9e6;
  }
  html, body {
    margin: 0;
    padding: 0;
    width: 1200px;
    height: 1200px;
    overflow: hidden;
    background: var(--canvas-bg);
  }
  .flyer {
    position: absolute;
    left: 195px;
    top: 30px;
    width: 810px;
    height: 1140px;
    display: block;
    background: var(--paper);
    font-family: "Montserrat", Arial, sans-serif;
  }
  .brand-name { fill: var(--brand-blue); font-weight: 600; font-size: 38px; }
  .callout { fill: var(--ink); font-size: 29px; }
  .callout .strong, .benefit .strong { font-weight: 700; }
  .headline { fill: #ffffff; font-size: 54px; font-weight: 400; letter-spacing: 1px; }
  .headline-bold { font-weight: 700; font-size: 58px; }
  .benefit { fill: var(--ink); font-size: 28px; font-weight: 400; }
  .contact { fill: #ffffff; font-size: 25px; font-weight: 400; text-anchor: middle; }
  .contact .strong { font-weight: 700; }
</style>
</head>
<body>
<svg class="flyer" viewBox="284 88 958 1350" xmlns="http://www.w3.org/2000/svg" font-family="Montserrat, Arial, sans-serif">
  <defs>
    <linearGradient id="blueBand" x1="0" y1="0" x2="1" y2="0">
      <stop offset="0" stop-color="var(--brand-blue-light)"/>
      <stop offset="1" stop-color="var(--brand-blue)"/>
    </linearGradient>
    <linearGradient id="blueBlock" x1="0" y1="0" x2="1" y2="1">
      <stop offset="0" stop-color="var(--brand-blue-light)"/>
      <stop offset="1" stop-color="var(--brand-blue-deep)"/>
    </linearGradient>
    <linearGradient id="photoTone" x1="0" y1="0" x2="1" y2="1">
      <stop offset="0" stop-color="var(--photo-green)"/>
      <stop offset="0.45" stop-color="var(--photo-warm)"/>
      <stop offset="1" stop-color="var(--photo-sky)"/>
    </linearGradient>
  </defs>

  <rect class="paper" x="284" y="88" width="958" height="1350" fill="var(--paper)"/>

  <!-- brand name -->
  <text class="brand-name" x="330" y="232">Brightquay Lending</text>
  <text class="brand-name" x="330" y="278">Services, Inc.</text>

  <!-- decorative geometry -->
  <polygon class="cream-stripe" points="1000,88 1070,88 700,458 630,458" fill="var(--cream)"/>
  <line class="accent-line" x1="987" y1="398" x2="1242" y2="150" stroke="var(--brand-blue)" stroke-width="8"/>
  <polygon class="accent-block" points="1190,235 1242,235 1242,458 970,458" fill="var(--brand-blue-light)"/>
  <polygon class="corner-block" points="284,396 600,396 600,458 284,700" fill="url(#blueBlock)"/>

  <!-- photo area -->
  <polygon class="hero-photo" role="img" aria-label="Photo: smiling construction worker in a yellow hard hat and safety vest, trees behind"
    points="284,700 560,458 1160,458 440,1172 284,1172" fill="url(#photoTone)"/>

  <polygon class="cream-stripe" points="650,965 712,965 512,1125 450,1125" fill="var(--cream)"/>

  <!-- headline band -->
  <polygon class="headline-band" points="860,743 1242,743 1242,965 650,965" fill="url(#blueBand)"/>

  <text class="callout" x="1205" y="670" text-anchor="end"><tspan class="strong">NO LICENSING</tspan></text>
  <text class="callout" x="1205" y="701" text-anchor="end">REQUIRED</text>

  <text class="headline" x="838" y="808" textLength="372" lengthAdjust="spacingAndGlyphs">HARD MONEY</text>
  <text class="headline" x="838" y="872" textLength="366" lengthAdjust="spacingAndGlyphs">ORIGINATORS</text>
  <text class="headline headline-bold" x="838" y="937" textLength="276" lengthAdjust="spacingAndGlyphs">WANTED</text>

  <!-- benefits -->
  <text class="benefit" x="672" y="1028" textLength="534" lengthAdjust="spacingAndGlyphs"><tspan class="strong">WORK AS</tspan> INDEPENDENT CONTRACTOR</text>
  <text class="benefit" x="672" y="1068" textLength="508" lengthAdjust="spacingAndGlyphs"><tspan class="strong">1% FLAT FINDERS FEE</tspan> ON EACH LOAN</text>
  <text class="benefit" x="672" y="1108" textLength="374" lengthAdjust="spacingAndGlyphs"><tspan class="strong">REFERRAL COMPENSATION</tspan></text>
  <text class="benefit" x="692" y="1147" textLength="500" lengthAdjust="spacingAndGlyphs">FOR RECRUITING NEW ORIGINATORS</text>
  <text class="benefit" x="672" y="1187" textLength="480" lengthAdjust="spacingAndGlyphs"><tspan class="strong">PROGRAMS</tspan> OFFERED NATIONWIDE</text>
  <text class="benefit" x="672" y="1227" textLength="346" lengthAdjust="spacingAndGlyphs"><tspan class="strong">MARKETING ASSISTANCE</tspan></text>
  <text class="benefit" x="692" y="1266" textLength="352" lengthAdjust="spacingAndGlyphs">AND SUPPORT AVAILABLE</text>

  <line class="divider" x1="603" y1="1145" x2="603" y2="1265" stroke="var(--ink)" stroke-width="1.5"/>
  <text class="callout" x="365" y="1236"><tspan class="strong">IMMEDIATE</tspan></text>
  <text class="callout" x="365" y="1267">PAYOUTS</text>

  <!-- contact footer -->
  <rect class="footer-band" x="284" y="1293" width="958" height="145" fill="url(#blueBand)"/>
  <polygon class="footer-stripe" points="1115,1438 1242,1313 1242,1338 1140,1438" fill="var(--paper)"/>
  <polygon class="footer-corner" points="1242,1383 1242,1438 1186,1438" fill="var(--brand-blue-deep)"/>
  <text class="contact" x="770" y="1322">Email <tspan class="strong">mpelton@brightquaylending.com</tspan> for more information</text>
  <text class="contact" x="770" y="1352">or call (800) 641-2950 Ext. 24</text>
  <text class="contact" x="770" y="1382">www.brightquaylending.com</text>
  <text class="contact" x="770" y="1411">NMLS #318760</text>
</svg>
</body>
</html>
```